New Townhome community needs for sale sign.

need a 4 foot by 8 foot banner to put on building listing newly constructed townhomes as "coming soon" to market. Construction is scheduled to be completed Dec 2024. Sale of units will begin Spring of 2025.
6 individual townhome units each 2,000 square feet. each unit is 3 bedroom 2.5 bathroom with 2 car garage and each has a rooftop "sky lounge" with amazing views. Gated community. Units available for sale Spring of 2025. Real estate company selling units will be KTL & Associates. Will need KTL & Associates Logo on the banner. Would like to keep with the same blue color scheme as the KTL & Associates logo. phone number on banner to be 480-555-3164. web ktlpartners.example.

```html
<!DOCTYPE html>
<html lang="en">
<head>
<meta charset="utf-8">
<title>KTL &amp; Associates – Coming Soon Banner</title>
<link rel="stylesheet" href="https://fonts.googleapis.com/css2?family=Barlow+Condensed:wght@500;600&display=swap">
<style>
  :root {
    --backdrop: #c3c3c3;
    --banner-white: #ffffff;
    --charcoal: #3a3a3c;
    --ink: #1e1e1e;
    --sky-blue: #23a6d9;
    --deep-blue: #1b6e9f;
    --type: "Barlow Condensed", "Arial Narrow", sans-serif;
  }
  html, body {
    margin: 0;
    width: 1200px;
    height: 1200px;
    overflow: hidden;
    background: var(--backdrop);
    font-family: var(--type);
  }
  .banner {
    position: absolute;
    left: 70px;
    top: 335px;
    width: 1060px;
    height: 530px;
    background: var(--banner-white);
    box-shadow: 0 4px 8px rgba(0,0,0,0.25);
    overflow: hidden;
  }
  .brand {
    position: absolute;
    left: 61px;
    top: 84px;
    display: flex;
    align-items: flex-end;
    gap: 18px;
  }
  .brand-mark {
    width: 100px;
    height: 100px;
    background: var(--sky-blue);
  }
  .brand-name {
    font-weight: 600;
    font-size: 62px;
    line-height: 0.8;
    color: var(--charcoal);
  }
  .headline-band {
    position: absolute;
    left: 0;
    top: 244px;
    width: 718px;
    height: 131px;
    background: var(--charcoal);
  }
  .headline {
    position: absolute;
    left: 61px;
    top: 50%;
    transform: translateY(-50%);
    margin: 0;
    font-weight: 500;
    font-size: 122px;
    line-height: 1;
    color: var(--banner-white);
    letter-spacing: 1px;
  }
  .completion-note {
    position: absolute;
    left: 61px;
    top: 420px;
    margin: 0;
    font-weight: 600;
    font-size: 27px;
    color: var(--ink);
    letter-spacing: 0.3px;
  }
  .info-panel {
    position: absolute;
    left: 0;
    top: 0;
    width: 1060px;
    height: 530px;
  }
  .sale-date, .contact {
    position: absolute;
    right: 59px;
    margin: 0;
    text-align: right;
    color: var(--banner-white);
    font-weight: 500;
    white-space: nowrap;
  }
  .sale-date {
    top: 72px;
    font-size: 49px;
    line-height: 50px;
  }
  .contact {
    top: 356px;
    font-size: 32px;
    line-height: 46px;
  }
</style>
</head>
<body>
  <section class="banner">
    <div class="brand">
      <div class="brand-mark"></div>
      <div class="brand-name">KTL &amp; Associates</div>
    </div>

    <div class="headline-band">
      <h1 class="headline">COMING SOON</h1>
    </div>

    <p class="completion-note">CONSTRUCTION IS SCHEDULED TO BE COMPLETED DEC 2024.</p>

    <svg class="info-panel" viewBox="0 0 1060 530" aria-hidden="true">
      <polygon points="717.5,77.5 1060,0 1060,269 717.5,350" fill="var(--sky-blue)"/>
      <polygon points="717.5,350 1060,269 1060,490 717.5,530" fill="var(--deep-blue)"/>
    </svg>

    <p class="sale-date">SALE OF<br>UNITS WILL<br>BEGIN SPRING<br>OF 2025.</p>
    <p class="contact">480-555-3164<br>KTLPARTNERS.EXAMPLE</p>
  </section>
</body>
</html>
```